Convert my PowerPoint mock up of a hiring process flow to simple, informative illustration with some

I need to create an illustration which is meant to be an overview of a hiring process for a medical training start up. I created a pretty rough PowerPoint mock up that hopefully shows what I am trying to do. My hope is that I would get the illustration created and can add it to my website. I have several other similar projects needed as well and probably ongoing graphic design work if we develop a good working relationship.

Site: www.brolvanhealth.com

Target Market(s)

Medical employers

Industry/Entity Type

Healthcare

Number of Pages Required

1 page

Font styles to use
Serif
Sans Serif

Colors
2fb6a2
85cae6

Requirements
Must have
• Simple illustration when done
Nice to have
• Fits very well with existing look and feel of site.
Should not have
• Not sure

```html
<!DOCTYPE html>
<html lang="en">
<head>
<meta charset="utf-8">
<title>Brolvan Health – Hiring Process</title>
<link href="https://fonts.googleapis.com/css2?family=Ruda:wght@700&family=Lato:wght@400;700&display=swap" rel="stylesheet">
<style>
:root{
  --teal:#2fb6a2;
  --teal-dark:#1f8f80;
  --sky:#85cae6;
  --ink:#1e2a2a;
  --muted:#4a5656;
  --card-border:#37b8a4;
  --white:#ffffff;
  --red:#f0321a;
  --orange:#f3a46a;
}
*{box-sizing:border-box;margin:0;padding:0}
html,body{width:1200px;height:849px;overflow:hidden}
body{
  position:relative;
  font-family:"Lato",sans-serif;color:var(--ink);
  background:
    radial-gradient(ellipse 700px 500px at 1150px 760px,rgba(245,160,110,.85),transparent 70%),
    radial-gradient(ellipse 600px 400px at 80px 820px,rgba(240,190,120,.6),transparent 70%),
    linear-gradient(160deg,#8ce6d4 0%,#9ef5dc 35%,#bdeeda 60%,#f2d2b0 100%);
}
.facets{position:absolute;inset:0}
.header{position:absolute;left:0;top:0;width:1200px;height:96px;background:rgba(255,255,255,.82)}
.brand{position:absolute;left:112px;top:36px;display:flex;align-items:center;gap:10px;
  font-family:"Ruda",sans-serif;font-weight:700;font-size:22px;color:#1b5fa8}
.brand-mark{width:22px;height:22px;border-radius:50%;background:#1b5fa8}
.phone{position:absolute;left:906px;top:36px;display:flex;align-items:center;gap:8px;
  font-family:"Ruda",sans-serif;font-weight:700;font-size:21px;color:var(--teal)}
.heading{position:absolute;font-family:"Ruda",sans-serif;font-weight:700;font-size:20.5px;
  line-height:27px;text-align:center;color:var(--ink)}
.resume-card{position:absolute;width:71px;height:84px;background:var(--white);
  border:1px solid var(--card-border);text-align:center;padding-top:8px}
.resume-card svg{display:block;margin:0 auto 2px}
.resume-card .label{font-family:"Ruda",sans-serif;font-weight:700;font-size:13.5px;line-height:17px}
.resume-card .sub{font-size:11.5px;color:var(--muted);letter-spacing:.3px}
.resume-card.finalist{background:var(--sky);border-color:var(--sky);color:var(--white)}
.resume-card.finalist .sub{color:var(--white)}
.panel{position:absolute;background:var(--white);border:1px solid var(--card-border)}
.avatar-ring{position:absolute;width:70px;height:70px;border-radius:50%;background:var(--white);
  border:4px solid var(--teal);display:flex;align-items:center;justify-content:center}
.body-copy{position:absolute;left:111px;top:438px;width:420px;text-align:center;font-size:14.5px;line-height:21.5px}
.step{position:absolute;left:645px;width:444px;background:var(--white);border:2px solid var(--teal);
  display:flex;align-items:center}
.step-icon{width:77px;height:100%;background:var(--teal);display:flex;align-items:center;justify-content:center;
  background-image:linear-gradient(135deg,transparent 55%,rgba(0,0,0,.15) 55%)}
.step-text{padding-left:16px;font-family:"Ruda",sans-serif;font-weight:700;font-size:19.5px;line-height:25px}
.finalist-btn{position:absolute;left:997px;top:505px;width:71px;height:35px;border-radius:4px;background:var(--teal);
  color:var(--white);font-family:"Ruda",sans-serif;font-weight:700;font-size:13.5px;letter-spacing:.5px;
  display:flex;align-items:center;justify-content:center}
.start-btn{position:absolute;left:779px;top:647px;width:163px;height:43px;background:var(--red);
  color:var(--white);font-family:"Ruda",sans-serif;font-weight:700;font-size:19px;
  display:flex;align-items:center;justify-content:center;gap:8px;border:1px solid #fff}
.caption{position:absolute;left:668px;top:524px;font-family:"Ruda",sans-serif;font-size:15px;font-weight:700;color:#333}
.footer{position:absolute;left:0;top:792px;width:1200px;height:50px;background:rgba(255,255,255,.6);
  display:flex;align-items:center;justify-content:center;font-size:13px;font-weight:700;color:#333}
.footer-strip{position:absolute;left:0;top:842px;width:1200px;height:7px;background:var(--orange)}
.lines{position:absolute;left:0;top:0}
</style>
</head>
<body>
<svg class="facets" width="1200" height="849" aria-hidden="true">
  <polygon points="0,96 300,96 0,500" fill="rgba(255,255,255,.12)"/>
  <polygon points="700,96 1200,96 1200,400" fill="rgba(255,255,255,.1)"/>
  <polygon points="400,500 900,792 200,792" fill="rgba(255,255,255,.08)"/>
  <polygon points="553,160 617,420 553,730 585,420" fill="rgba(60,160,140,.35)"/>
</svg>

<header class="header">
  <div class="brand"><span class="brand-mark"></span>Brolvan Health</div>
  <div class="phone">
    <svg width="22" height="22" viewBox="0 0 22 22"><circle cx="11" cy="11" r="10" fill="none" stroke="#333" stroke-width="1.6"/><path d="M7.5 6.5l2 -0.5 1 2.5-1.3 1c.6 1.4 1.4 2.2 2.8 2.8l1-1.3 2.5 1-.5 2c-3.5.3-7.8-4-7.5-7.5z" fill="#333"/></svg>
    0100 -555-0142
  </div>
</header>

<svg width="0" height="0" style="position:absolute">
  <defs>
    <symbol id="user" viewBox="0 0 36 36">
      <circle cx="18" cy="18" r="17" fill="#bfe3f3" stroke="#6fbfe0" stroke-width="1.2"/>
      <circle cx="18" cy="14" r="6" fill="#6fbfe0"/>
      <path d="M7 30c1-6 5-9 11-9s10 3 11 9a16 16 0 0 1-22 0z" fill="#6fbfe0"/>
    </symbol>
    <symbol id="person" viewBox="0 0 36 36">
      <circle cx="18" cy="10" r="6" fill="#222"/>
      <path d="M6 32c0-8 5-13 12-13s12 5 12 13z" fill="#222"/>
      <path d="M16 19h4l-1 8h-2z" fill="#fff"/>
    </symbol>
  </defs>
</svg>

<!-- Left column -->
<div class="resume-card" style="left:111px;top:134px"><svg width="36" height="36"><use href="#user"/></svg><div class="label">Resume</div><div class="sub">CSV File</div></div>
<div class="resume-card" style="left:198px;top:134px"><svg width="36" height="36"><use href="#user"/></svg><div class="label">Resume</div><div class="sub">CSV File</div></div>
<div class="resume-card" style="left:286px;top:134px"><svg width="36" height="36"><use href="#user"/></svg><div class="label">Resume</div><div class="sub">CSV File</div></div>
<div class="resume-card" style="left:373px;top:134px"><svg width="36" height="36"><use href="#user"/></svg><div class="label">Resume</div><div class="sub">CSV File</div></div>
<div class="resume-card" style="left:461px;top:134px"><svg width="36" height="36"><use href="#user"/></svg><div class="label">Resume</div><div class="sub">CSV File</div></div>

<div class="heading" style="left:111px;top:238px;width:428px">Collect and Synthesize Candidates<br>for Training, Employment</div>

<div class="panel" style="left:111px;top:388px;width:420px;height:154px"></div>
<div class="avatar-ring" style="left:286px;top:353px"><svg width="36" height="36"><use href="#person"/></svg></div>
<p class="body-copy">Lorem ipsum dolor sit amet, consectetuer adipiscin elit, sedml diam nonummy nibh euismod tincidunt ut laoreet dolore magna aliquam erat volutpat Lorem ipsum dolor sit amet, consectetuer Lorem ipsum dolor sit amet, consectetuer.</p>

<div class="heading" style="left:111px;top:559px;width:428px">Employer Selects Their Favored<br>Candidates To Interview</div>

<div class="resume-card" style="left:111px;top:681px"><svg width="36" height="36"><use href="#user"/></svg><div class="label">Resume</div><div class="sub">CSV File</div></div>
<div class="resume-card" style="left:198px;top:681px"><svg width="36" height="36"><use href="#user"/></svg><div class="label">Resume</div><div class="sub">CSV File</div></div>
<div class="resume-card" style="left:286px;top:681px"><svg width="36" height="36"><use href="#user"/></svg><div class="label">Resume</div><div class="sub">CSV File</div></div>
<div class="resume-card" style="left:373px;top:681px"><svg width="36" height="36"><use href="#user"/></svg><div class="label">Resume</div><div class="sub">CSV File</div></div>
<div class="resume-card" style="left:461px;top:681px"><svg width="36" height="36"><use href="#user"/></svg><div class="label">Resume</div><div class="sub">CSV File</div></div>

<!-- Right column -->
<div class="step" style="top:134px;height:84px">
  <div class="step-icon"><svg width="44" height="40" viewBox="0 0 44 40" fill="#fff"><rect x="16" y="2" width="26" height="16" fill="none" stroke="#fff" stroke-width="2"/><circle cx="9" cy="8" r="4"/><path d="M3 22c0-5 3-8 6-8l8-4 1 2-7 5v5z"/><circle cx="8" cy="27" r="3"/><circle cx="17" cy="27" r="3"/><circle cx="26" cy="27" r="3"/><circle cx="35" cy="27" r="3"/><path d="M3 38c0-4 2-6 5-6s5 2 5 6zM12 38c0-4 2-6 5-6s5 2 5 6zM21 38c0-4 2-6 5-6s5 2 5 6zM30 38c0-4 2-6 5-6s5 2 5 6z"/></svg></div>
  <div class="step-text">Employer,Brolvan Health Agree Upon<br>Training Protocol</div>
</div>

<div class="panel" style="left:645px;top:317px;width:444px;height:248px"></div>
<div class="avatar-ring" style="left:833px;top:281px"><svg width="36" height="36"><use href="#person"/></svg></div>
<div class="heading" style="left:645px;top:366px;width:444px">Candidates Interviewed By Employer</div>

<div class="resume-card" style="left:674px;top:402px"><svg width="36" height="36"><use href="#user"/></svg><div class="label">Resume</div><div class="sub">CSV File</div></div>
<div class="resume-card" style="left:761px;top:402px"><svg width="36" height="36"><use href="#user"/></svg><div class="label">Resume</div><div class="sub">CSV File</div></div>
<div class="resume-card" style="left:849px;top:402px"><svg width="36" height="36"><use href="#user"/></svg><div class="label">Resume</div><div class="sub">CSV File</div></div>
<div class="resume-card finalist" style="left:999px;top:402px"><svg width="36" height="36"><use href="#user"/></svg><div class="label">Resume</div><div class="sub">CSV File</div></div>
<div class="caption">Candidates Interviewed By Employer</div>
<div class="finalist-btn">FINALIST</div>

<div class="step" style="top:578px;height:50px">
  <div class="step-icon"><svg width="36" height="32" viewBox="0 0 36 32" fill="none" stroke="#fff" stroke-width="2"><circle cx="11" cy="8" r="5"/><path d="M2 28c0-7 4-11 9-11s9 4 9 11z"/><circle cx="25" cy="14" r="4"/><rect x="19" y="20" width="15" height="9"/></svg></div>
  <div class="step-text">Brolvan Health Pre-Employment Training</div>
</div>

<div class="start-btn">
  <svg width="22" height="20" viewBox="0 0 22 20" fill="#fff"><rect x="1" y="8" width="5" height="11"/><path d="M8 8l4-7c2 0 3 1 2.5 3l-1 3h6c1.5 0 2.3 1.2 2 2.5l-2 8c-.3 1-1 1.5-2 1.5H8z"/></svg>
  START JOB!
</div>

<div class="step" style="top:715px;height:50px">
  <div class="step-icon"><svg width="30" height="32" viewBox="0 0 30 32" fill="#fff"><circle cx="15" cy="10" r="6"/><path d="M7 10a8 8 0 0 1 16 0" fill="none" stroke="#fff" stroke-width="2"/><path d="M3 31c0-7 5-12 12-12s12 5 12 12z"/></svg></div>
  <div class="step-text">Post Employment Support (1-3 months)</div>
</div>

<svg class="lines" width="1200" height="849" aria-hidden="true">
  <g fill="#4d7f77">
    <path d="M312 310h26l-13 25z"/>
    <path d="M856 236h26l-13 26z"/>
  </g>
  <g stroke="var(--teal)" stroke-width="1.2" fill="var(--teal)">
    <path d="M147 633H510M147 633v35M235 633v35M324 633v35M412 633v35M510 633v35" fill="none"/>
    <circle cx="147" cy="668" r="3"/><circle cx="235" cy="668" r="3"/><circle cx="324" cy="668" r="3"/><circle cx="412" cy="668" r="3"/><circle cx="510" cy="668" r="3"/>
    <path d="M713 486v29H885M797 486v29M885 486v29" fill="none"/>
    <circle cx="713" cy="515" r="3"/><circle cx="797" cy="515" r="3"/><circle cx="885" cy="515" r="3"/>
  </g>
  <g fill="none" stroke="#cfd6d6" stroke-width="2.5">
    <path d="M936 420l9 10-9 10M945 420l9 10-9 10M954 420l9 10-9 10"/>
    <path d="M936 455l9 10-9 10M945 455l9 10-9 10M954 455l9 10-9 10"/>
  </g>
</svg>

<footer class="footer">Copyright©&nbsp; 2015 Brolvan Health. All Rights Reserved.</footer>
<div class="footer-strip"></div>
</body>
</html>
```